New Business Card Design Project

possibly double-sided card, with one side in color. leaves, a tree branch, or a tree of life, like laurel, olive, pine ... or a seed that grows. visual discreet and stylized or naive. no photo. no human silhouette Modern Typo possibly rounded corners matte paper, no selective varnish, neither gold nor silver English brief Double sided business card, with eventually a single colored side. Leaves, a tree branch or a tree of life, laurel, olive tree, pine tree ... or a growing seed. The design has to be discreet and stylized or naive. No human silhouettes Modern made Possibly rounded corners Matte paper, no selective varnish, no gold, no silver
Updates

I really prefer toned or subtles tones, Bluish / greenwich gray, verdigris ... Elegant and discreet colors Write "HUMANISTIC HYPNOTHERAPY, SYMBOLIC THERAPY" on 2 lines and on One side only (not with the name and address) Not use pictogram (such , address...)

Contact Information for Business Card

Hypnothérapie humaniste
Thérapie symbolique

Mireille Fontanel
Hypnothérapeute
06 48 17 35 82
84 rue des Glycines, 33320 Eysines
therapie.fontanel@exemplemail.fr

Colors
33b8a4
3176b5

Requirements
Must have
• sober, elegant and refined card Sober design, elegant, plain
Nice to have
• desired colors: gray, blue-gis, greyish, khaki ... Desired colors: gray, blue-gray, grayish green, khaki, ...
Should not have
• gaudy colors, bright greens no bright gold neon colors

```html
<!DOCTYPE html>
<html lang="fr">
<head>
<meta charset="UTF-8">
<title>Carte de visite – Hypnothérapie humaniste</title>
<link rel="stylesheet" href="https://fonts.googleapis.com/css2?family=Cormorant+Garamond:ital,wght@0,500;1,500&display=swap">
<style>
  :root {
    --backdrop: #c9c9c9;
    --card-paper: #f3f3f1;
    --leaf-light: #c3dcd2;
    --leaf-mid: #a3c7b9;
    --leaf-deep: #8fb8a8;
    --ink: #2e4843;
  }
  * { margin: 0; padding: 0; box-sizing: border-box; }
  html, body {
    width: 1200px;
    height: 800px;
    overflow: hidden;
    background: var(--backdrop);
  }
  .stage {
    position: relative;
    width: 1200px;
    height: 800px;
    display: flex;
    align-items: center;
    justify-content: center;
  }
  .business-card {
    position: relative;
    width: 960px;
    height: 620px;
    border-radius: 44px;
    overflow: hidden;
    background: var(--card-paper);
  }
  .leaf-frame {
    position: absolute;
    inset: 0;
    background: linear-gradient(135deg, var(--leaf-light) 0%, var(--leaf-mid) 50%, var(--leaf-deep) 100%);
  }
  .card-field {
    position: absolute;
    top: 58px;
    left: 58px;
    right: 58px;
    bottom: 58px;
    background: var(--card-paper);
    display: flex;
    align-items: center;
    justify-content: center;
  }
  .practice-title {
    font-family: "Cormorant Garamond", serif;
    font-weight: 500;
    font-size: 30px;
    line-height: 1.2;
    letter-spacing: 0.08em;
    text-transform: uppercase;
    text-align: center;
    color: var(--ink);
  }
  .practice-title em {
    font-style: italic;
  }
</style>
</head>
<body>
  <main class="stage">
    <section class="business-card">
      <div class="leaf-frame" role="img" aria-label="Frise de feuilles stylisées vert-de-gris encadrant la carte"></div>
      <div class="card-field">
        <h1 class="practice-title">
          Hypnoth<em>e</em>rapie hum<em>a</em>niste,<br>
          Th<em>e</em>rapie symbolique
        </h1>
      </div>
    </section>
  </main>
</body>
</html>
```